Book Cover Design for Millennial

I need a book cover design for my book Sunward Ledger. The subtitle of the book is Seven Quiet Steps Toward Steady Ground at Work.

I'm a career coach who helps millennial career professionals. I myself am a millennial but on the older end (34). I've dealt and been through most of the challenges millennials are facing as career professionals and I wrote this book with the thought of providing guidance and aid to getting past those challenges and shedding light on fundamental habits and practices that will help them excel in their careers. In addition, the book will help them prepare millennials for our turn as the leaders, managers, etc moving forward in corporate America. The final design should have the main title of the book in it as the focal point but not the subtitle. I want the cover to communicate something NEW, Bold, Youthful, non-traditional. I want it to stick out while still maintaining a sleek and Professional look.
Updates

Hello, Designers! I want to thank you all for your submissions! The work is amazing and I greatly appreciate it. If you would I want to help out in this process by adding a few updates based on the submissions I have seen. The concept I think that is coming close to hitting the mark is Bramble Forja. What I would like to see changed about the concept is the following: Change the outfits to be more Millennial Career Professional. I have attached some ideas to the brief. I want to replace this picture with one of multiple millennials anywhere from 3 and up. I would like the pic to have diversity in it representing most races of people in the USA. I would like my name beneath sunward ledger. I'm not a known author yet so having my name that big my distract from the title of the book. Can we make the title a little bigger and so far I like the background.Thanks, DP Added Friday, September 30, 2016

Target Market(s)

Millennial Career Professionals (18 - 34 age group)

Industry/Entity Type

Life Coaching

Logo Text

Sunward Ledger

Requirements
Must have
• communicate something NEW, Bold, Youthful, non-traditional. I want it to stick out while still maintaining a sleek and Professional look.
Nice to have
• something that goes with my brand
• http://www.doranpelwick.com
Should not have
• Nothing 3D or a logo that is hard to read when placed on stationeries, business cards etc

```html
<!DOCTYPE html>
<html lang="en">
<head>
<meta charset="utf-8">
<title>Sunward Ledger — Book Cover</title>
<link rel="stylesheet" href="https://fonts.googleapis.com/css2?family=Bebas+Neue&family=Noto+Serif&family=Oswald:wght@600&display=swap">
<style>
  :root {
    --page-bg: #f4f4f4;
    --cover-bg: #ffffff;
    --gold-deep: #f3b415;
    --gold-light: #f3dc35;
    --ink: #111111;
    --rule: #1a1a1a;
    --suit-dark: #1b2233;
    --suit-mid: #3b4458;
  }
  * { margin: 0; padding: 0; box-sizing: border-box; }
  html, body {
    width: 1200px;
    height: 1135px;
    overflow: hidden;
    background: var(--page-bg);
  }
  .book-cover {
    position: absolute;
    left: 255px;
    top: 30px;
    width: 690px;
    height: 1075px;
    background: var(--cover-bg);
    box-shadow: 0 6px 24px rgba(0, 0, 0, 0.12);
    overflow: hidden;
  }
  .title {
    position: absolute;
    top: 28px;
    left: 0;
    width: 100%;
    text-align: center;
    font-family: "Bebas Neue", "Oswald", sans-serif;
    font-size: 188px;
    line-height: 0.84;
    letter-spacing: 0.01em;
    background: linear-gradient(90deg, var(--gold-deep) 0%, var(--gold-light) 50%, var(--gold-deep) 100%);
    -webkit-background-clip: text;
    background-clip: text;
    color: transparent;
  }
  .title span { display: block; }
  .subtitle-block {
    position: absolute;
    top: 372px;
    left: 115px;
    width: 460px;
    padding: 12px 0 14px;
    border-top: 2px solid var(--rule);
    border-bottom: 2px solid var(--rule);
    text-align: center;
  }
  .subtitle {
    font-family: "Noto Serif", "Cambria", serif;
    font-size: 33px;
    line-height: 1.2;
    color: var(--ink);
  }
  .team-photo {
    position: absolute;
    top: 548px;
    left: 16px;
    width: 658px;
    height: 390px;
    background: linear-gradient(180deg, var(--suit-mid) 0%, var(--suit-dark) 100%);
    clip-path: polygon(0 0, 100% 0, 100% 12%, 54% 100%, 46% 100%, 0 12%);
  }
  .author-band {
    position: absolute;
    left: 0;
    bottom: 0;
    width: 100%;
    height: 124px;
    background: linear-gradient(90deg, var(--gold-deep) 0%, var(--gold-light) 50%, var(--gold-deep) 100%);
    display: flex;
    align-items: center;
    justify-content: center;
  }
  .author-name {
    font-family: "Oswald", sans-serif;
    font-weight: 600;
    font-size: 46px;
    letter-spacing: 0.2em;
    color: var(--ink);
  }
</style>
</head>
<body>
  <main class="book-cover">
    <h1 class="title"><span>Sunward</span><span>Ledger</span></h1>
    <div class="subtitle-block">
      <p class="subtitle">Seven Quiet Steps Toward<br>Steady Ground at Work</p>
    </div>
    <div class="team-photo" role="img" aria-label="Photo of a diverse group of young professionals in business suits standing in a V formation, a smiling leader at the front"></div>
    <footer class="author-band">
      <p class="author-name">AUTHOR NAME</p>
    </footer>
  </main>
</body>
</html>
```